Chimney Service company needs new business card design

We need a updated business card with our new logo added. We provide a full range of chimney services throughout Vermont and New Hampshire. The business card will be one sided and color. Attached is our current business card another document showing all the information we would like on the card.
We dont like a lot of flashy colors.... here is a link to our website to get an idea of our branding www.flueguardianvt.example

Target Market(s)

homeowners

Industry/Entity Type

Business

Contact Information for Business Card

See attached sheet for content.

Font styles to use
Serif
Sans Serif

Requirements
Must have
• all information provided on separate sheet
Should not have
• Additional information that may clogg up design

```html
<!DOCTYPE html>
<html lang="en">
<head>
<meta charset="utf-8">
<title>Flue Guardian – Business Card</title>
<link rel="stylesheet" href="https://fonts.googleapis.com/css2?family=Tinos:ital,wght@0,400;0,700;1,400&display=swap">
<style>
  :root {
    --page-bg: #e8e5e0;
    --card-white: #f7f7f7;
    --charcoal: #2f2f2f;
    --charcoal-band: #353535;
    --ink: #333333;
    --ember-red: #a31d1d;
    --white: #ffffff;
    --smoke: rgba(0, 0, 0, 0.06);
    --smoke-light: rgba(255, 255, 255, 0.05);
  }
  * { margin: 0; padding: 0; box-sizing: border-box; }
  html, body {
    width: 900px;
    height: 1200px;
    overflow: hidden;
    background: var(--page-bg);
  }
  .canvas { position: relative; width: 900px; height: 1200px; }

  .card {
    position: absolute;
    left: 78px;
    width: 744px;
    overflow: hidden;
    font-family: "Tinos", "Times New Roman", serif;
  }

  /* Front */
  .card-front { top: 145px; height: 433px; background: var(--card-white); }
  .flame-decor-front {
    position: absolute; left: 600px; top: 0; width: 144px; height: 262px;
    background: radial-gradient(ellipse at 50% 60%, var(--smoke) 0%, rgba(0,0,0,0) 70%);
  }
  .brand-lockup {
    position: absolute; left: 40px; top: 160px; width: 300px;
    display: flex; align-items: center; justify-content: center; gap: 12px;
  }
  .brand-square { width: 22px; height: 22px; background: var(--ink); }
  .brand-name {
    font-size: 30px; font-weight: 400; letter-spacing: 1px;
    color: var(--ink); text-transform: uppercase; white-space: nowrap;
  }
  .services {
    position: absolute; left: 396px; top: 58px; list-style: none;
  }
  .services li {
    display: flex; align-items: center; height: 36px;
    font-size: 16.5px; color: var(--ink); text-transform: uppercase; letter-spacing: 0.2px;
  }
  .services li::before {
    content: ""; width: 8px; height: 8px; margin-right: 12px;
    background: var(--ember-red); transform: rotate(45deg);
  }
  .divider-dark {
    position: absolute; left: 0; top: 263px; width: 100%; height: 7px; background: var(--charcoal);
  }
  .contact-band {
    position: absolute; left: 0; top: 275px; width: 100%; height: 143px; background: var(--charcoal-band);
  }
  .flame-decor-band {
    position: absolute; right: 0; top: 0; width: 56px; height: 143px;
    background: linear-gradient(100deg, rgba(255,255,255,0) 20%, #f2f2f2 60%, var(--charcoal-band) 95%);
  }
  .contact-list { position: absolute; left: 44px; top: 33px; list-style: none; color: var(--white); }
  .contact-list li { display: flex; align-items: center; height: 26px; font-size: 18px; }
  .contact-list li.phone { font-size: 21px; font-weight: 700; }
  .contact-list svg { width: 17px; height: 17px; margin-right: 9px; fill: none; stroke: var(--white); stroke-width: 1.5; }
  .contact-list li.phone svg { fill: var(--white); stroke: none; }
  .taglines {
    position: absolute; right: 30px; top: 30px; text-align: right;
    font-style: italic; font-size: 19px; line-height: 29px; color: var(--white);
  }
  .taglines span { display: block; }
  .taglines .indent-1 { margin-right: 22px; }
  .taglines .indent-2 { margin-right: 31px; }
  .accent-stripe {
    position: absolute; left: 0; bottom: 0; width: 100%; height: 13px;
    background: var(--ember-red); border-top: 2px solid var(--white);
  }

  /* Back */
  .card-back { top: 627px; height: 435px; background: var(--charcoal); }
  .flame-decor-back {
    position: absolute; left: 420px; top: 0; width: 300px; height: 435px;
    background: radial-gradient(ellipse at 50% 55%, var(--smoke-light) 0%, rgba(255,255,255,0) 65%);
  }
  .card-back .brand-lockup { left: 0; top: 190px; width: 744px; }
  .card-back .brand-square { background: var(--white); }
  .card-back .brand-name { color: var(--white); }
</style>
</head>
<body>
<main class="canvas">
  <section class="card card-front" aria-label="Business card front">
    <div class="flame-decor-front" role="img" aria-label="Faint flame decoration"></div>
    <div class="brand-lockup">
      <span class="brand-square"></span>
      <span class="brand-name">Flue Guardian</span>
    </div>
    <ul class="services">
      <li>Full Masonry Services</li>
      <li>Historic Chimney Restoration</li>
      <li>Stainless Steel Liners</li>
      <li>New Chimney Installations</li>
      <li>HFGA Certified Chimney Sweeps</li>
    </ul>
    <div class="divider-dark"></div>
    <div class="contact-band">
      <ul class="contact-list">
        <li class="phone">
          <svg viewBox="0 0 24 24" aria-hidden="true"><path d="M6.6 10.8a15 15 0 0 0 6.6 6.6l2.2-2.2c.3-.3.7-.4 1-.2 1.1.4 2.3.6 3.6.6.6 0 1 .4 1 1V20c0 .6-.4 1-1 1A17 17 0 0 1 3 4c0-.6.4-1 1-1h3.5c.6 0 1 .4 1 1 0 1.3.2 2.5.6 3.6.1.3 0 .7-.2 1z"/></svg>
          802-555-0147
        </li>
        <li>
          <svg viewBox="0 0 24 24" aria-hidden="true"><rect x="2.5" y="5" width="19" height="14"/><path d="M2.5 5l9.5 8 9.5-8M2.5 19l7-7M21.5 19l-7-7"/></svg>
          info@flueguardianvt.example
        </li>
        <li>
          <svg viewBox="0 0 24 24" aria-hidden="true"><circle cx="12" cy="12" r="9.5"/><ellipse cx="12" cy="12" rx="4" ry="9.5"/><path d="M2.5 12h19M4 7h16M4 17h16"/></svg>
          www.flueguardianvt.example
        </li>
      </ul>
      <p class="taglines">
        <span>Family owned and operated</span>
        <span class="indent-1">Fully insured – Free estimates</span>
        <span class="indent-2">Serving VT and NH since 1989</span>
      </p>
      <div class="flame-decor-band" role="img" aria-label="White flame swirl decoration"></div>
    </div>
    <div class="accent-stripe"></div>
  </section>

  <section class="card card-back" aria-label="Business card back">
    <div class="flame-decor-back" role="img" aria-label="Faint large flame decoration"></div>
    <div class="brand-lockup">
      <span class="brand-square"></span>
      <span class="brand-name">Flue Guardian</span>
    </div>
  </section>
</main>
</body>
</html>
```